Bluff Marigold

Need a site for a cbd dispensary texas theme. We sell all federal and legal hemp products

Target Market(s)

Cbd and other hemp derivatives

Industry/Entity Type

Hemp derivatives

Coding

Coded - Design and coding required

Number of Pages Required

3 page

Font styles to use
Sans Serif

Colors
0094D4
00A9DD
6FCCEA
C7EBF8
E9F6FB

Requirements
Must have
• Integration for bigcommerce shopping
Nice to have
• Easy layout for shopping

```html
<!DOCTYPE html>
<html lang="en">
<head>
<meta charset="utf-8">
<title>Bluff Marigold — Hemp &amp; CBD</title>
<link href="https://fonts.googleapis.com/css2?family=Montserrat:wght@400;500;600;700;800&display=swap" rel="stylesheet">
<style>
:root{
  --blue:#0A79C9;
  --blue-bright:#0094D4;
  --sky:#6FCCEA;
  --pale:#E9F6FB;
  --pale-2:#DDEFF8;
  --ink:#1b1b1b;
  --text:#333;
  --muted:#666;
  --line:#cfcfcf;
  --footer:#232323;
  --white:#fff;
}
*{margin:0;padding:0;box-sizing:border-box}
html,body{width:1200px;height:3697px;overflow:hidden}
body{font-family:'Montserrat',sans-serif;color:var(--text);background:var(--white);position:relative}
.abs{position:absolute}
.btn{position:absolute;background:var(--blue);color:var(--white);font-weight:700;text-transform:uppercase;display:flex;align-items:center;justify-content:center;letter-spacing:.3px}
.btn-sm{font-size:10.5px;height:28px}
.ph{position:absolute}

/* header */
.logo{position:absolute;left:130px;top:32px;font-size:26px;font-weight:700;color:var(--blue);line-height:1.05;width:150px}
.search{left:431px;top:18px;width:280px;height:32px;border:1.5px solid #555;display:flex}
.search span{flex:1;font-size:10px;padding:9px 12px;color:#444}
.search b{width:36px;background:var(--blue);display:flex;align-items:center;justify-content:center}
.call{left:745px;top:16px;display:flex;gap:12px;align-items:center}
.call .sep{width:1px;height:34px;background:#555}
.call small{display:block;font-size:11px;color:#333}
.call strong{font-size:17px;font-weight:500;color:#111}
.cart{left:952px;top:0;width:117px;height:50px;background:var(--blue);color:var(--white);display:flex;align-items:center;gap:10px;padding-left:10px;font-size:9.5px;line-height:1.4}
.nav{left:431px;top:74px;display:flex;font-size:13.5px;font-weight:500;color:#222}
.nav a{color:inherit;text-decoration:none;margin-right:0}
.nav .active{color:var(--blue);text-decoration:underline}

/* hero */
.hero{left:0;top:108px;width:1200px;height:586px;background:linear-gradient(90deg,#e6e8e9 0%,#d2d6d6 45%,#a8a882 65%,#5e7d3c 85%,#3f6a2a 100%)}
.hero h1{position:absolute;left:128px;top:115px;font-size:58px;font-weight:800;color:var(--blue);letter-spacing:.5px}
.hero p{position:absolute;left:130px;top:197px;font-size:22px;line-height:1.4;color:#222;width:400px}
.dots{position:absolute;left:563px;top:537px;display:flex;gap:9px;align-items:center}
.dots i{width:6px;height:6px;border-radius:50%;background:#fff;display:block}
.dots i.on{width:10px;height:10px;border:2px solid var(--white);background:var(--blue)}

/* tiles */
.tile{position:absolute;top:703px;width:387px;height:232px;color:var(--white)}
.tile h3{position:absolute;left:25px;top:32px;font-size:22px;font-weight:800;line-height:1.1}
.tile p{position:absolute;left:25px;top:92px;font-size:12px;line-height:1.35;width:125px}
.tile .btn{left:25px;top:172px;width:86px;height:27px;font-size:10.5px}

/* section heads */
.sec-title{position:absolute;left:0;width:1200px;text-align:center;font-size:20px;font-weight:700;color:#111}
.sec-title::after{content:"";display:block;width:62px;height:1.5px;background:#444;margin:18px auto 0}

/* product cards */
.card{position:absolute;width:226px;height:355px;border:1px solid var(--line);background:var(--white);overflow:hidden}
.card .img{position:absolute;left:10px;top:12px;width:204px;height:180px}
.card h4{position:absolute;top:226px;width:100%;text-align:center;font-size:13px;font-weight:600;color:#222}
.card .price{position:absolute;top:254px;width:100%;text-align:center;font-size:19px;color:#111}
.card .price s{font-size:13px;color:#555;margin-right:6px}
.card .btn{left:62px;top:292px;width:102px;height:29px;font-size:10.5px}
.badge{position:absolute;left:0;top:0;width:0;height:0;border-top:56px solid var(--blue);border-right:56px solid transparent}
.badge span{position:absolute;left:2px;top:-48px;transform:rotate(-45deg);color:#fff;font-size:10px;white-space:nowrap;transform-origin:left top;margin-top:40px}
.arrow{position:absolute}

/* welcome */
.welcome-img{left:0;top:1464px;width:574px;height:406px;background:linear-gradient(135deg,#a3303e 0%,#7a1c2a 45%,#d9a98a 75%,#e8c59f 100%)}
.welcome{left:574px;top:1464px;width:626px;height:406px;background:var(--pale-2)}
.welcome small{position:absolute;left:49px;top:48px;font-size:18px;color:#222}
.welcome h2{position:absolute;left:49px;top:68px;font-size:28px;font-weight:800;color:#111}
.welcome p{position:absolute;left:49px;top:138px;width:448px;font-size:14.5px;line-height:22.5px;color:#333}
.welcome .btn{left:52px;top:326px;width:101px;height:29px}

/* banner */
.banner{left:0;top:2412px;width:1200px;height:398px;background:linear-gradient(135deg,#4c9a5f 0%,#3f8a53 50%,#4a9a5d 100%)}
.banner h2{position:absolute;top:123px;width:100%;text-align:center;color:#fff;font-size:28px;font-weight:800;line-height:40px}
.banner .btn{left:527px;top:216px;width:147px;height:48px;font-size:16px;border:2px solid #fff}

/* blog */
.blog{left:0;top:2810px;width:1200px;height:538px;background:var(--pale)}
.post{position:absolute;top:122px;width:292px;height:361px;background:#fff}
.post .img{position:absolute;left:0;top:0;width:292px;height:158px}
.post h4{position:absolute;left:25px;top:188px;width:250px;font-size:13px;font-weight:600;line-height:22px;color:#111}
.post p{position:absolute;left:25px;top:244px;width:240px;font-size:11.5px;line-height:15.5px;color:#333}
.post .btn{left:26px;top:303px;width:93px;height:28px}

/* footer */
.footer{left:0;top:3348px;width:1200px;height:349px;background:var(--footer);color:#eee}
.f-logo{position:absolute;left:130px;top:80px;font-size:40px;font-weight:700;color:var(--blue);line-height:1.05;width:220px}
.f-col h5{font-size:12.5px;font-weight:700;color:#fff;margin-bottom:22px}
.f-col ul{list-style:none;font-size:11.5px;line-height:19.5px}
.f-row{display:flex;gap:12px;align-items:center;font-size:11.5px;line-height:16px;margin-bottom:19px}
.f-row i{width:24px;height:24px;border-radius:50%;background:#fff;display:flex;align-items:center;justify-content:center;flex:none}
.f-line{position:absolute;left:130px;top:262px;width:939px;height:1px;background:#444}
.copy{position:absolute;top:306px;width:100%;text-align:center;font-size:9.5px;color:#ddd}
</style>
</head>
<body>

<header>
  <div class="logo">Bluff Marigold</div>
  <div class="abs search"><span>SEARCH</span><b><svg width="14" height="14" viewBox="0 0 14 14"><circle cx="6" cy="6" r="4.2" fill="none" stroke="#fff" stroke-width="1.8"/><line x1="9" y1="9" x2="12.5" y2="12.5" stroke="#fff" stroke-width="1.8"/></svg></b></div>
  <div class="abs call">
    <svg width="26" height="26" viewBox="0 0 24 24"><path d="M6.6 10.8a15 15 0 0 0 6.6 6.6l2.2-2.2c.3-.3.7-.4 1-.2 1.1.4 2.3.6 3.6.6.6 0 1 .4 1 1V20c0 .6-.4 1-1 1A17 17 0 0 1 3 4c0-.6.4-1 1-1h3.5c.6 0 1 .4 1 1 0 1.3.2 2.5.6 3.6.1.3 0 .7-.2 1z" fill="none" stroke="#333" stroke-width="1.5"/></svg>
    <div class="sep"></div>
    <div><small>CALL US</small><strong>888.888.8888</strong></div>
  </div>
  <div class="abs cart">
    <svg width="16" height="14" viewBox="0 0 16 14"><path d="M0 1h3l2 8h8l2-6H4" fill="none" stroke="#fff" stroke-width="1.6"/><circle cx="6" cy="12" r="1.3" fill="#fff"/><circle cx="12" cy="12" r="1.3" fill="#fff"/></svg>
    <div>MY CART (0)<br>$0.00</div>
  </div>
  <nav class="abs nav">
    <a class="active" style="margin-right:39px">HOME</a>
    <a style="margin-right:44px">ABOUT US</a>
    <a style="margin-right:47px">PRODUCTS</a>
    <a style="margin-right:46px">CATEGORIES</a>
    <a style="margin-right:39px">SHOP</a>
    <a>CONTACT US</a>
  </nav>
</header>

<section class="abs hero" role="img" aria-label="Dropper releasing hemp oil into a glass bottle beside seeds on a wooden spoon and green hemp leaves">
  <h1>HEMP OIL</h1>
  <p>Lorem Ipsum is simply dummy text of the printing and typesetting.</p>
  <div class="btn" style="left:130px;top:286px;width:151px;height:50px;font-size:16px">SHOP NOW</div>
  <div class="dots"><i></i><i></i><i class="on"></i><i></i><i></i></div>
</section>

<section>
  <div class="tile" style="left:10px;background:linear-gradient(120deg,#159a86 0%,#1aa48c 45%,#c9b98a 80%,#a9927a 100%)" role="img" aria-label="Tins of hemp balm with lavender and a hemp leaf on teal">
    <h3>LOREM<br>IPSUM</h3><p>Lorem Ipsum is simply dummy text of the printing and typesetting.</p><div class="btn">SHOP NOW</div>
  </div>
  <div class="tile" style="left:405px;background:linear-gradient(120deg,#1f5e2a 0%,#3f8b3a 50%,#8a4c1e 75%,#2f6b2c 100%)" role="img" aria-label="Amber dropper bottle of hemp oil among hemp leaves">
    <h3>HEMP<br>OIL</h3><p>Lorem Ipsum is simply dummy text of the printing and typesetting.</p><div class="btn">SHOP NOW</div>
  </div>
  <div class="tile" style="left:803px;background:linear-gradient(120deg,#5b6a54 0%,#8c8f7c 45%,#d8d2c2 75%,#b9a77d 100%)" role="img" aria-label="Handmade hemp soap bars tied with twine beside a loofah">
    <h3>HEMP<br>SOAP</h3><p>Lorem Ipsum is simply dummy text of the printing and typesetting.</p><div class="btn">SHOP NOW</div>
  </div>
</section>

<section>
  <h2 class="sec-title" style="top:981px">OUR PRODUCTS</h2>
  <svg class="arrow" style="left:72px;top:1216px" width="14" height="22" viewBox="0 0 14 22"><path d="M11 2 3 11l8 9" fill="none" stroke="#777" stroke-width="2"/></svg>
  <svg class="arrow" style="left:1096px;top:1216px" width="14" height="22" viewBox="0 0 14 22"><path d="M3 2l8 9-8 9" fill="none" stroke="#777" stroke-width="2"/></svg>

  <div class="card" style="left:130px;top:1057px"><div class="img" role="img" aria-label="CBD dropper bottles and vape pen with hemp buds" style="background:radial-gradient(ellipse at 50% 55%,#6b4a2b 0%,#9a8a6e 35%,#fff 70%)"></div><h4>LOREM IPSUM</h4><div class="price">$25.00</div><div class="btn">ADD TO CART</div></div>
  <div class="card" style="left:368px;top:1057px"><div class="img" role="img" aria-label="Stacked bars of orange hemp soap" style="background:radial-gradient(ellipse at 50% 50%,#c0632a 0%,#e6a36a 35%,#f6f2ee 62%,#fff 75%)"></div><h4>LOREM IPSUM</h4><div class="price">$25.00</div><div class="btn">ADD TO CART</div></div>
  <div class="card" style="left:606px;top:1057px"><div class="img" role="img" aria-label="Bottles of golden hemp oil with seeds and softgel capsules" style="background:radial-gradient(ellipse at 50% 50%,#e5c21a 0%,#f2dd6a 30%,#fff 65%)"></div><h4>LOREM IPSUM</h4><div class="price">$25.00</div><div class="btn">ADD TO CART</div></div>
  <div class="card" style="left:843px;top:1057px"><div class="img" role="img" aria-label="Hemp leaf beside a heap of green hemp powder" style="background:radial-gradient(ellipse at 50% 50%,#5f8a32 0%,#a7b77a 35%,#fff 68%)"></div><h4>LOREM IPSUM</h4><div class="price">$25.00</div><div class="btn">ADD TO CART</div></div>
</section>

<section>
  <div class="abs welcome-img" role="img" aria-label="Hand holding a hemp gummy ring in front of a gummy pouch"></div>
  <div class="abs welcome">
    <small>WELCOME TO</small>
    <h2>BLUFF MARIGOLD.</h2>
    <p>There are many variations of passages of Lorem Ipsum available, but the majority have suffered alteration in some form, by injected humour, or randomised words which don't look even slightly believable. If you are going to use a passage of Lorem Ipsum, you need to be sure there isn't anything embarrassing hidden in the middle of text. All the Lorem Ipsum generators on the Internet tend to repeat</p>
    <div class="btn btn-sm">READ MORE</div>
  </div>
</section>

<section>
  <h2 class="sec-title" style="top:1920px">SPECIAL OFFERS</h2>
  <svg class="arrow" style="left:72px;top:2160px" width="14" height="22" viewBox="0 0 14 22"><path d="M11 2 3 11l8 9" fill="none" stroke="#777" stroke-width="2"/></svg>
  <svg class="arrow" style="left:1096px;top:2160px" width="14" height="22" viewBox="0 0 14 22"><path d="M3 2l8 9-8 9" fill="none" stroke="#777" stroke-width="2"/></svg>

  <div class="card" style="left:130px;top:2001px"><div class="img" role="img" aria-label="Amber bottles with hemp leaves and capsules" style="background:radial-gradient(ellipse at 50% 50%,#4a2e1a 0%,#8a7a52 35%,#fff 68%)"></div><div class="badge"><span>10% OFF</span></div><h4>LOREM IPSUM</h4><div class="price"><s>$45.00</s>$25.00</div><div class="btn">ADD TO CART</div></div>
  <div class="card" style="left:368px;top:2001px"><div class="img" role="img" aria-label="Glass jar filled with dried hemp flower" style="background:radial-gradient(ellipse at 50% 50%,#3f5a2a 0%,#8a9a78 35%,#fff 65%)"></div><div class="badge"><span>15% OFF</span></div><h4>LOREM IPSUM</h4><div class="price"><s>$45.00</s>$25.00</div><div class="btn">ADD TO CART</div></div>
  <div class="card" style="left:608px;top:2001px"><div class="img" role="img" aria-label="Wooden bowl of green hemp powder" style="background:radial-gradient(circle at 50% 50%,#b4b277 0%,#9aa064 30%,#a0663a 42%,#fff 58%)"></div><div class="badge"><span>5% OFF</span></div><h4>LOREM IPSUM</h4><div class="price"><s>$45.00</s>$25.00</div><div class="btn">ADD TO CART</div></div>
  <div class="card" style="left:843px;top:2001px"><div class="img" role="img" aria-label="Pile of green hemp capsules" style="left:0;top:0;width:226px;height:188px;background:linear-gradient(135deg,#4f6a3a 0%,#9fae85 40%,#55703c 70%,#c3cbb2 100%)"></div><div class="badge"><span>12% OFF</span></div><h4>LOREM IPSUM</h4><div class="price"><s>$45.00</s>$25.00</div><div class="btn">ADD TO CART</div></div>
</section>

<section class="abs banner" role="img" aria-label="Flat lay of cosmetic bottles, tubes and hemp leaves on green">
  <h2>LOREM IPSUM IS SIMPLY DUMMY<br>TEXT OF THE PRINTING</h2>
  <div class="btn">SHOP NOW</div>
</section>

<section class="abs blog">
  <h2 class="sec-title" style="top:46px">LATEST BLOG</h2>
  <article class="post" style="left:130px"><div class="img" role="img" aria-label="Jar of hemp cream with leaves on dark wood" style="background:linear-gradient(120deg,#5a4636 0%,#9c8874 40%,#4c6a2e 70%,#3f3024 100%)"></div><h4>LOREM IPSUM IS SIMPLY DUMMY TEXT OF THE PRINTING</h4><p>There are many variations of passages of Lorem Ipsum available, but the majority have suffered alteratio.</p><div class="btn btn-sm">READ MORE</div></article>
  <article class="post" style="left:454px"><div class="img" role="img" aria-label="Hemp seeds, spoon and a carafe of oil on marble" style="background:linear-gradient(120deg,#e9e6e2 0%,#d2cbc0 45%,#d9b13a 75%,#efece7 100%)"></div><h4>LOREM IPSUM IS SIMPLY DUMMY TEXT OF THE PRINTING</h4><p>There are many variations of passages of Lorem Ipsum available, but the majority have suffered alteratio.</p><div class="btn btn-sm">READ MORE</div></article>
  <article class="post" style="left:776px"><div class="img" role="img" aria-label="Red cup of hemp tea with leaves on a wooden table" style="background:linear-gradient(120deg,#3c5a26 0%,#8a3a22 40%,#c0482c 60%,#6a4a2c 100%)"></div><h4>LOREM IPSUM IS SIMPLY DUMMY TEXT OF THE PRINTING</h4><p>There are many variations of passages of Lorem Ipsum available, but the majority have suffered alteratio.</p><div class="btn btn-sm">READ MORE</div></article>
</section>

<footer class="abs footer">
  <div class="f-logo">Bluff Marigold</div>
  <div class="abs f-col" style="left:475px;top:52px">
    <h5>MENU</h5>
    <ul><li>HOME</li><li>ABOUT US</li><li>PRODUCTS</li><li>CATEGORIES</li><li>SHOP</li><li>CONTACT US</li></ul>
  </div>
  <div class="abs f-col" style="left:665px;top:52px">
    <h5>CONTACT US</h5>
    <div class="f-row"><i><svg width="10" height="12" viewBox="0 0 10 12"><path d="M5 0a4 4 0 0 0-4 4c0 3 4 8 4 8s4-5 4-8a4 4 0 0 0-4-4z" fill="#222"/><circle cx="5" cy="4" r="1.4" fill="#fff"/></svg></i><span>2217 Caprock Lane<br>Amarillo, TX 79101</span></div>
    <div class="f-row"><i><svg width="11" height="11" viewBox="0 0 24 24"><path d="M6.6 10.8a15 15 0 0 0 6.6 6.6l2.2-2.2c.3-.3.7-.4 1-.2 1.1.4 2.3.6 3.6.6.6 0 1 .4 1 1V20c0 .6-.4 1-1 1A17 17 0 0 1 3 4c0-.6.4-1 1-1h3.5c.6 0 1 .4 1 1 0 1.3.2 2.5.6 3.6.1.3 0 .7-.2 1z" fill="#222"/></svg></i><span>Call Us<br>888.888.8888</span></div>
    <div class="f-row"><i><svg width="12" height="9" viewBox="0 0 12 9"><rect x=".5" y=".5" width="11" height="8" fill="none" stroke="#222"/><path d="M.5.5 6 5 11.5.5" fill="none" stroke="#222"/></svg></i><span>E mail Us<br>info@BluffMarigold.com</span></div>
  </div>
  <div class="abs f-col" style="left:957px;top:52px">
    <h5>FOLLOW US</h5>
    <div class="f-row"><i></i><span>Like us on<br>FRIENDBOARD</span></div>
    <div class="f-row"><i></i><span>Follow us on<br>CHIRPLINE</span></div>
    <div class="f-row"><i></i><span>Follow us on<br>WORKLINK</span></div>
  </div>
  <div class="f-line"></div>
  <div class="copy">Copyright © 2021 All Rights Reserved</div>
</footer>

</body>
</html>
```